Belcotti Business Cards

Business cards for real estate
Target Market(s)
Real estate
Industry/Entity Type
Real Estate Agent
Font styles to use
Serif
Requirements
Must have
- Photo and logo

```html
<!DOCTYPE html>
<html lang="en">
<head>
<meta charset="utf-8">
<title>Belcotti Realty Business Cards</title>
<link rel="stylesheet" href="https://fonts.googleapis.com/css2?family=Cinzel:wght@400;600&family=Tinos:wght@400;700&display=swap">
<style>
  :root {
    --page-bg: #2b2b2d;
    --maroon: #7a1d2a;
    --maroon-dark: #5e1520;
    --copper: #a85a35;
    --copper-light: #c27a48;
    --ink: #1b1b1b;
    --cream: #f6ead8;
    --lime: #9fd23a;
    --white: #ffffff;
    --sky: #e7ebf2;
    --lawn: #cfd8c0;
  }
  html, body {
    margin: 0;
    width: 1200px;
    height: 852px;
    overflow: hidden;
    background: var(--page-bg);
  }
  .sheet {
    width: 1200px;
    height: 852px;
    display: flex;
    align-items: center;
    justify-content: center;
    gap: 40px;
  }
  .card {
    width: 560px;
    height: 320px;
    display: block;
    filter: drop-shadow(0 10px 18px rgba(0,0,0,.45));
  }
  .brand-name { font-family: "Cinzel", Georgia, serif; font-weight: 400; }
  .site-url { font-family: "Cinzel", Georgia, serif; letter-spacing: 3px; }
  .agent-name { font-family: "Tinos", "Times New Roman", serif; font-weight: 700; letter-spacing: 1px; }
  .agent-title { font-family: "Tinos", "Times New Roman", serif; }
  .contact-line { font-family: "Tinos", "Times New Roman", serif; }
</style>
</head>
<body>
<main class="sheet">

  <!-- Front of card -->
  <svg class="card card-front" viewBox="0 0 560 320" xmlns="http://www.w3.org/2000/svg">
    <defs>
      <clipPath id="front-shape"><rect width="560" height="320" rx="22"/></clipPath>
      <linearGradient id="scene-tone" x1="0" y1="0" x2="0" y2="1">
        <stop offset="0" stop-color="var(--sky)"/>
        <stop offset=".55" stop-color="#dcdad6"/>
        <stop offset="1" stop-color="var(--lawn)"/>
      </linearGradient>
      <linearGradient id="copper-sweep" x1="0" y1="1" x2="1" y2="0">
        <stop offset="0" stop-color="var(--maroon)"/>
        <stop offset=".5" stop-color="var(--copper)"/>
        <stop offset="1" stop-color="var(--maroon-dark)"/>
      </linearGradient>
      <linearGradient id="night-panel" x1="0" y1="0" x2="1" y2="1">
        <stop offset="0" stop-color="#2a2a2a"/>
        <stop offset="1" stop-color="#0d0d0d"/>
      </linearGradient>
    </defs>
    <g clip-path="url(#front-shape)">
      <rect class="house-scene" width="560" height="320" fill="url(#scene-tone)" role="img" aria-label="Faded photo of a suburban house with a lawn"/>
      <path class="dark-panel" d="M440,0 L560,0 L560,250 C520,255 470,250 440,238 C470,160 470,80 440,0 Z" fill="url(#night-panel)"/>
      <path class="copper-sweep" d="M0,272 C200,252 350,190 410,60 C420,35 425,15 425,0 L440,0 C470,80 470,160 440,238 C500,262 540,262 560,258 L560,320 L0,320 Z" fill="url(#copper-sweep)"/>
      <path class="sweep-line-white" d="M0,262 C200,242 350,180 405,55 C414,32 418,15 418,0" fill="none" stroke="var(--white)" stroke-width="9"/>
      <path class="sweep-line-black" d="M0,272 C200,252 350,190 410,60" fill="none" stroke="var(--ink)" stroke-width="5"/>
      <path class="sweep-line-red" d="M432,0 C462,80 462,160 432,238" fill="none" stroke="var(--maroon)" stroke-width="4"/>
      <rect class="footer-band" x="0" y="286" width="560" height="34" fill="var(--maroon)"/>
      <text class="site-url" x="60" y="309" font-size="12" fill="var(--cream)">WWW.BELCOTTIREALTY.COM</text>

      <g class="brand-lockup">
        <circle cx="118" cy="120" r="36" fill="var(--maroon)"/>
        <text class="brand-name" x="170" y="118" font-size="40" fill="var(--ink)">BELCOTTI</text>
        <text class="brand-name" x="172" y="152" font-size="26" letter-spacing="9" fill="var(--ink)">REALTY</text>
      </g>
    </g>
  </svg>

  <!-- Back of card -->
  <svg class="card card-back" viewBox="0 0 560 320" xmlns="http://www.w3.org/2000/svg">
    <defs>
      <clipPath id="back-shape"><rect width="560" height="320" rx="22"/></clipPath>
      <linearGradient id="maroon-top" x1="0" y1="0" x2="1" y2="1">
        <stop offset="0" stop-color="var(--maroon-dark)"/>
        <stop offset=".6" stop-color="var(--maroon)"/>
        <stop offset="1" stop-color="#9a3a34"/>
      </linearGradient>
      <linearGradient id="copper-base" x1="0" y1="0" x2="1" y2="1">
        <stop offset="0" stop-color="var(--copper)"/>
        <stop offset=".5" stop-color="var(--copper-light)"/>
        <stop offset="1" stop-color="var(--maroon)"/>
      </linearGradient>
      <linearGradient id="portrait-tone" x1="0" y1="0" x2="0" y2="1">
        <stop offset="0" stop-color="#e9e6e3"/>
        <stop offset=".35" stop-color="#b08e78"/>
        <stop offset=".55" stop-color="#2c2f3a"/>
        <stop offset="1" stop-color="#1c1e26"/>
      </linearGradient>
    </defs>
    <g clip-path="url(#back-shape)">
      <rect class="copper-base" width="560" height="320" fill="url(#copper-base)"/>
      <rect class="maroon-header" width="560" height="170" fill="url(#maroon-top)"/>
      <line class="divider" x1="240" y1="176" x2="560" y2="176" stroke="var(--white)" stroke-width="3"/>
      <line class="divider-thin" x1="240" y1="183" x2="560" y2="183" stroke="var(--white)" stroke-width="1"/>

      <path class="photo-panel" d="M0,95 C120,82 230,120 272,180 C300,225 302,280 282,320 L0,320 Z" fill="var(--white)"/>
      <rect class="agent-photo" x="40" y="135" width="210" height="185" rx="40" fill="url(#portrait-tone)" role="img" aria-label="Portrait photo of the agent in a dark suit"/>

      <g class="brand-lockup">
        <circle cx="318" cy="100" r="30" fill="var(--white)"/>
        <text class="brand-name" x="362" y="88" font-size="34" fill="var(--white)">BELCOTTI</text>
        <text class="brand-name" x="364" y="122" font-size="23" letter-spacing="8" fill="var(--white)">REALTY</text>
      </g>

      <text class="agent-name" x="300" y="203" font-size="16" fill="var(--cream)">YOUR NAME HERE</text>
      <text class="agent-title" x="300" y="218" font-size="11" fill="var(--lime)">Realtor ®</text>

      <g class="contact-block" text-anchor="end" fill="var(--cream)" font-size="10.5">
        <text class="contact-line" x="520" y="228">2740 Linden Court</text>
        <text class="contact-line" x="520" y="242">Suite 4, Ashford, VT 05102</text>
        <text class="contact-line" x="520" y="258">0712-5550-1948</text>
        <text class="contact-line" x="520" y="274">0945-5550-3371</text>
        <text class="contact-line" x="520" y="290">info@belcottirealty.com</text>
        <text class="contact-line" x="520" y="306">www.belcottirealty.com</text>
      </g>

      <g class="contact-icons" fill="var(--lime)">
        <rect class="icon-mobile" x="529" y="248" width="7" height="12" rx="1.5"/>
        <path class="icon-phone" d="M528,265 q2,-2 4,0 l1,2 q-1,2 1,4 q2,2 4,1 l2,1 q2,2 0,4 q-6,1 -10,-4 q-4,-4 -2,-8 Z"/>
        <rect class="icon-mail" x="527" y="283" width="12" height="8"/>
        <circle class="icon-web" cx="533" cy="302" r="6"/>
      </g>

      <g class="membership-badges" fill="var(--white)">
        <rect x="300" y="270" width="16" height="16"/>
        <rect x="324" y="270" width="16" height="16"/>
      </g>
    </g>
  </svg>

</main>
</body>
</html>
```